Webbanner-Design für Slideshow
Zielgruppe
Annegret bietet 3 Kurse an:
diese Kurse verhelfen einem selbst seine Schutzengel wieder zu hören,
mit ihnen ihren Seelenplan weshalb man auf Erden ist zu sehen,
sowie professionell umzusetzen.
Zielgruppe:
Spirituelle Menschen,
welche Engel lieben,
an sich mental gerne in Kursen & Privat arbeiten,
neues Wissen sich liebend gerne aneignen,
ihren Seelenplan wissen und umsetzen möchten,
die Schönheit im Inneren (Seele) und
im Aussen (Körper & Umgebung) lieben.
Aufgabenstellung
Produktbannerbild für meine Website (Slideshow):
Hintergrund: vorhanden in Form von einem Jpeg, hier auf diesem Foto bitte dich einfach mit folgendem beschäftigen:
Schriftzug groß: Engel (wieder) hören lernen & deinen Seelenplan umsetzen
mit Annegret Holzmeier (klein, oder großer Schriftzug?)
Schriftzug klein: mehr …
Schriftfarbe: weiss
Schriftart: moderne Schrift (z.Bsp. was die Zeitschriften benützen)
Haus Button Schriftzug: KURSE IN MUC
Buttons Ideen, Vierecke oder Kreise ect.: Transparent bitte und in passender Farbe
Stil: Modern, klar, schön, nicht verschnörkelt, unesoterisch, unverspielt
Mein Logo mit Flügel: irgendwo miteinbauen
Sonstiges: anbei noch ein Iconzeichen für Kurse Seminar
Auflösung Farbe: Text & Icons für Druck (Flyer) & Webproduktpräsentation (Slideshow)
Maße: (bei 1600xca.872 px., bleiben, Banner nicht verkleinern, oder ranzoomen)

```html
<!DOCTYPE html>
<html lang="de">
<head>
<meta charset="utf-8">
<title>Engel hören lernen – Kurse in München</title>
<link rel="stylesheet" href="https://fonts.googleapis.com/css2?family=Cinzel:wght@400;500&family=Tinos:ital@1&display=swap">
<style>
  :root{
    --bg-rose:#e4d4d4;
    --bg-light:#fbf6f5;
    --white:#ffffff;
    --mauve-text:#b49d9d;
    --band:#c2a7a9;
    --band-dark:#b3979a;
    --photo-warm:#efe2de;
    --photo-rose:#e8cfcc;
    --bloom:#f3d3d2;
  }
  *{margin:0;padding:0;box-sizing:border-box}
  html,body{width:1200px;height:654px;overflow:hidden;background:var(--bg-light)}
  .banner{
    position:relative;width:1200px;height:654px;overflow:hidden;
    background:
      radial-gradient(ellipse 520px 300px at 420px 360px, rgba(255,255,255,.95), rgba(255,255,255,0) 70%),
      linear-gradient(125deg, var(--bg-rose) 0%, #eee2e1 30%, var(--bg-light) 55%, #f4e9e8 100%);
  }
  .bloom-area{
    position:absolute;left:0;top:300px;width:600px;height:260px;
    background:
      radial-gradient(circle 90px at 90px 130px, rgba(243,211,210,.55), rgba(243,211,210,0) 70%),
      radial-gradient(circle 80px at 250px 170px, rgba(243,211,210,.45), rgba(243,211,210,0) 70%),
      radial-gradient(circle 70px at 470px 180px, rgba(243,211,210,.35), rgba(243,211,210,0) 70%);
  }
  .photo-area{
    position:absolute;right:0;top:0;width:620px;height:654px;
    background:
      radial-gradient(ellipse 150px 200px at 330px 400px, rgba(232,207,204,.9), rgba(232,207,204,0) 75%),
      radial-gradient(ellipse 200px 150px at 300px 120px, rgba(224,205,205,.7), rgba(224,205,205,0) 75%),
      linear-gradient(180deg, var(--photo-warm), #f6eeec);
    -webkit-mask-image:linear-gradient(90deg, transparent 0%, #000 28%, #000 92%, transparent 100%);
            mask-image:linear-gradient(90deg, transparent 0%, #000 28%, #000 92%, transparent 100%);
  }
  .brand{
    position:absolute;left:22px;top:56px;
    font-family:'Cinzel',serif;font-size:15px;color:var(--white);
    text-shadow:none;letter-spacing:1px;
  }
  .headline{
    position:absolute;left:124px;top:40px;
    font-family:'Cinzel',serif;font-weight:400;font-size:92px;line-height:1;
    color:var(--white);letter-spacing:2px;
    text-shadow:0 2px 6px rgba(120,90,90,.35);
  }
  .subline{
    position:absolute;left:36px;top:168px;
    font-family:'Tinos',serif;font-style:italic;font-size:39px;line-height:48px;
    color:var(--mauve-text);
  }
  .host{
    position:absolute;left:37px;top:455px;
    font-family:'Tinos',serif;font-style:italic;font-size:31px;
    color:var(--mauve-text);
  }
  .course-band{
    position:absolute;left:0;top:539px;width:100%;height:115px;
    background:linear-gradient(90deg, var(--band-dark) 0%, var(--band) 30%, rgba(194,167,169,.5) 48%, rgba(194,167,169,0) 62%);
    display:flex;align-items:center;padding-left:26px;
  }
  .course-band svg{flex:none}
  .course-label{
    margin-left:24px;
    font-family:'Cinzel',serif;font-size:34px;color:var(--white);letter-spacing:1px;
  }
</style>
</head>
<body>
<div class="banner">
  <div class="bloom-area" role="img" aria-label="Zart verschwommene rosa Rosen im Hintergrund"></div>
  <div class="photo-area" role="img" aria-label="Foto: Kursleiterin am weißen Schreibtisch mit Stift und Notizbuch, dahinter Kaminsims mit Herzrahmen und Rosen"></div>

  <div class="brand">Seelenweg</div>
  <h1 class="headline">ENGEL</h1>
  <p class="subline">(wieder) hören lernen<br>&amp; deinen Seelenplan<br>umsetzen</p>
  <p class="host">mit Annegret Holzmeier</p>

  <div class="course-band">
    <svg width="70" height="70" viewBox="0 0 70 70" aria-hidden="true">
      <circle cx="35" cy="35" r="32" fill="none" stroke="#fff" stroke-width="2.5"/>
      <path d="M18 36 L35 21 L52 36" fill="none" stroke="#fff" stroke-width="3" stroke-linejoin="round" stroke-linecap="round"/>
      <path d="M23 33 V49 H31 V40 H39 V49 H47 V33" fill="none" stroke="#fff" stroke-width="2.5" stroke-linejoin="round"/>
      <rect x="44" y="22" width="4" height="8" fill="#fff"/>
    </svg>
    <span class="course-label">KURSE IN MUC</span>
  </div>
</div>
</body>
</html>
```